Coffee Shop needs a fresh new menu

Hi,
I would like a new menu to be designed for our coffee shop.
We display our menu on a television screen, so would need it in a file that would allow us to continue to do so -- I have attached a photo so that you can see our current design, and how it is displayed.

I'd like something that is easy to read, if the design could have a "hipster" feel to it -- we are located at a hospital and University.

I have attached a Word file with what we would like on the menu.

Feel free to contact me if you have any questions.

Thanks,
Liv

Just A4 size will be fine, and no need to include menu 1 and menu 2 - I just put them in as an example of what we already have -- they are our printed menu's. Thanks

Hospital

```html
<!DOCTYPE html>
<html lang="en">
<head>
<meta charset="utf-8">
<title>Ward Brew Canteen Menu</title>
<link rel="stylesheet" href="https://fonts.googleapis.com/css2?family=Arimo:wght@400;700&family=Nunito:wght@400;700;800&display=swap">
<style>
  :root {
    --bg: #48413f;
    --ink: #f4f1ef;
    --mint: #bfe6e6;
    --mint-dark: #98cacb;
    --pink: #f7d4e1;
    --pink-dark: #e2b3c6;
    --ribbon-text: #4a4341;
    --glow-mint: rgba(191, 230, 230, 0.10);
    --glow-pink: rgba(247, 212, 225, 0.13);
  }
  * { margin: 0; padding: 0; box-sizing: border-box; }
  html, body { width: 1200px; height: 848px; overflow: hidden; background: var(--bg); }
  .menu {
    position: relative;
    width: 1200px;
    height: 848px;
    overflow: hidden;
    background: var(--bg);
    font-family: "Nunito", sans-serif;
    color: var(--ink);
  }

  .art { position: absolute; }
  .art--mint { background: radial-gradient(closest-side, var(--glow-mint), rgba(191, 230, 230, 0) 100%); }
  .art--pink { background: radial-gradient(closest-side, var(--glow-pink), rgba(247, 212, 225, 0) 100%); }

  .brand {
    position: absolute;
    left: 80px; top: 262px; width: 200px;
    text-align: center;
    font-weight: 800;
    font-size: 30px;
    line-height: 34px;
    color: var(--pink);
  }

  .ribbon { position: absolute; }
  .ribbon svg { position: absolute; inset: 0; width: 100%; height: 100%; }
  .ribbon__label {
    position: absolute; inset: 0;
    display: flex; align-items: center; justify-content: center;
    font-weight: 800;
    font-size: 18px;
    color: var(--ribbon-text);
    padding-bottom: 12px;
  }

  .coffee-table {
    position: absolute;
    left: 469px; top: 86px;
    font-family: "Arimo", sans-serif;
    font-size: 18px;
    border-collapse: collapse;
  }
  .coffee-table th { font-weight: 700; text-align: left; height: 24px; }
  .coffee-table td { height: 24px; padding: 0; white-space: nowrap; }
  .coffee-table .drink { width: 149px; }
  .coffee-table .size-s { width: 67px; }
  .coffee-table .price { color: var(--mint); font-weight: 700; }

  .list {
    position: absolute;
    text-align: center;
    list-style: none;
    font-size: 17px;
    line-height: 24px;
    white-space: nowrap;
  }
  .list .price { color: var(--mint); font-weight: 800; }
  .list--short { font-family: "Arimo", sans-serif; font-size: 18px; letter-spacing: 0.5px; }
  .list--short .price { font-weight: 700; }

  .extras {
    position: absolute;
    left: 250px; top: 416px; width: 710px;
    text-align: center;
    font-family: "Arimo", sans-serif;
    font-size: 18px;
    letter-spacing: 0.5px;
    line-height: 25px;
    white-space: nowrap;
  }
  .extras__title { color: var(--mint); font-weight: 700; }
  .extras .price { color: var(--mint); font-weight: 700; }
</style>
</head>
<body>
<main class="menu">

  <div class="art art--mint" style="left:30px;top:0;width:300px;height:380px" role="img" aria-label="Hanging sign frame on chains with arrow bar, heart, flowers and flourish"></div>
  <div class="art art--mint" style="left:340px;top:0;width:60px;height:50px" role="img" aria-label="Small bird on the sign bar"></div>
  <div class="art art--pink" style="left:325px;top:92px;width:95px;height:115px" role="img" aria-label="Line drawn bird"></div>
  <div class="art art--pink" style="left:838px;top:24px;width:56px;height:52px" role="img" aria-label="Two tone heart"></div>
  <div class="art art--mint" style="left:776px;top:152px;width:96px;height:112px" role="img" aria-label="Line drawn bird"></div>
  <div class="art art--mint" style="left:880px;top:0;width:200px;height:360px" role="img" aria-label="Hanging birdcage line drawing"></div>
  <div class="art art--pink" style="left:1094px;top:92px;width:96px;height:115px" role="img" aria-label="Line drawn bird"></div>
  <div class="art art--pink" style="left:1118px;top:10px;width:66px;height:36px" role="img" aria-label="Small heart key"></div>
  <div class="art art--pink" style="left:366px;top:326px;width:68px;height:54px" role="img" aria-label="Heart with flourish"></div>
  <div class="art art--pink" style="left:772px;top:346px;width:58px;height:50px" role="img" aria-label="Small heart key"></div>
  <div class="art art--pink" style="left:1042px;top:364px;width:54px;height:50px" role="img" aria-label="Heart on a leaf stem"></div>
  <div class="art art--pink" style="left:10px;top:370px;width:56px;height:54px" role="img" aria-label="Small heart key"></div>
  <div class="art art--mint" style="left:555px;top:470px;width:108px;height:22px" role="img" aria-label="Small flourish divider"></div>
  <div class="art art--pink" style="left:360px;top:682px;width:94px;height:116px" role="img" aria-label="Pink bird silhouette"></div>
  <div class="art art--mint" style="left:766px;top:624px;width:92px;height:108px" role="img" aria-label="Mint bird silhouette"></div>
  <div class="art art--pink" style="left:1132px;top:680px;width:58px;height:54px" role="img" aria-label="Two tone heart"></div>
  <div class="art art--pink" style="left:20px;top:756px;width:58px;height:54px" role="img" aria-label="Two tone heart"></div>
  <div class="art art--mint" style="left:130px;top:764px;width:116px;height:20px" role="img" aria-label="Small flourish divider"></div>
  <div class="art art--pink" style="left:562px;top:794px;width:90px;height:26px" role="img" aria-label="Small flourish divider"></div>
  <div class="art art--mint" style="left:972px;top:808px;width:86px;height:22px" role="img" aria-label="Small flourish divider"></div>

  <div class="brand">Ward Brew</div>

  <!-- Coffee -->
  <div class="ribbon" style="left:500px;top:8px;width:236px;height:72px">
    <svg viewBox="0 0 236 72" preserveAspectRatio="none" aria-hidden="true">
      <polygon points="0,28 40,28 40,66 0,66 14,47" fill="var(--mint-dark)"/>
      <polygon points="236,28 196,28 196,66 236,66 222,47" fill="var(--mint-dark)"/>
      <path d="M28,10 Q118,-4 208,10 L208,54 Q118,40 28,54 Z" fill="var(--mint)"/>
    </svg>
    <div class="ribbon__label">Coffee</div>
  </div>

  <table class="coffee-table">
    <thead>
      <tr><th></th><th class="size-s">&nbsp;&nbsp;S</th><th>&nbsp;&nbsp;L</th></tr>
    </thead>
    <tbody>
      <tr><td class="drink">Latte</td><td class="price">$4.0</td><td class="price">$4.50</td></tr>
      <tr><td class="drink">Cappuccino</td><td class="price">$4.0</td><td class="price">$4.50</td></tr>
      <tr><td class="drink">Flat White</td><td class="price">$4.0</td><td class="price">$4.50</td></tr>
      <tr><td class="drink">Long Black</td><td class="price">$4.0</td><td class="price">$4.50</td></tr>
      <tr><td class="drink">Hot Chocolate</td><td class="price">$4.0</td><td class="price">$4.50</td></tr>
      <tr><td class="drink">Chai Latte</td><td class="price">$4.50</td><td class="price">&nbsp;$5.0</td></tr>
      <tr><td class="drink">Mocha</td><td class="price">$4.50</td><td class="price">&nbsp;$5.0</td></tr>
      <tr><td class="drink">Dirty Chai</td><td class="price">$5</td><td class="price">&nbsp;$5.50</td></tr>
    </tbody>
  </table>

  <ul class="list list--short" style="left:450px;top:312px;width:310px">
    <li>Espresso <span class="price">$3.50</span></li>
    <li>Short Macchiato <span class="price">$4.0</span></li>
    <li>Piccolo <span class="price">$4.0</span></li>
    <li>Long Macchiato <span class="price">$4.50</span></li>
  </ul>

  <div class="extras">
    <p class="extras__title">EXTRAS</p>
    <p>Soy Milk/Lactose Free Milk/Syrups/Extra Shot/Decaf&nbsp; <span class="price">$0.50</span> extra</p>
  </div>

  <!-- Breakfast -->
  <div class="ribbon" style="left:30px;top:446px;width:322px;height:84px;transform:rotate(3deg)">
    <svg viewBox="0 0 322 84" preserveAspectRatio="none" aria-hidden="true">
      <polygon points="0,36 60,36 60,80 0,80 20,58" fill="var(--mint-dark)"/>
      <polygon points="322,36 262,36 262,80 322,80 302,58" fill="var(--mint-dark)"/>
      <path d="M40,12 Q161,-4 282,12 L282,64 Q161,48 40,64 Z" fill="var(--mint)"/>
    </svg>
    <div class="ribbon__label">Breakfast</div>
  </div>

  <ul class="list" style="left:20px;top:543px;width:330px">
    <li>Bacon, Egg and Cheese Roll <span class="price">$6.0</span></li>
    <li>Ham and Cheese Toastie <span class="price">$5.0</span></li>
    <li>Cheese and Tomato Toastie <span class="price">$5.0</span></li>
    <li>Ham and Cheese Croissant <span class="price">$6.0</span></li>
    <li>Cheese and Tomato Croissant <span class="price">$5.50</span></li>
    <li>Plain Croissant <span class="price">$3.50</span></li>
    <li>Hash Brown <span class="price">$2.0</span></li>
    <li>2 Piece Toast <span class="price">$3.0</span></li>
    <li>2 Piece Rasin Toast <span class="price">$3.0</span></li>
  </ul>

  <!-- Something Light -->
  <div class="ribbon" style="left:452px;top:506px;width:310px;height:84px;transform:rotate(2deg)">
    <svg viewBox="0 0 310 84" preserveAspectRatio="none" aria-hidden="true">
      <polygon points="0,36 58,36 58,80 0,80 20,58" fill="var(--pink-dark)"/>
      <polygon points="310,36 252,36 252,80 310,80 290,58" fill="var(--pink-dark)"/>
      <path d="M38,12 Q155,-4 272,12 L272,64 Q155,48 38,64 Z" fill="var(--pink)"/>
    </svg>
    <div class="ribbon__label">Something Light</div>
  </div>

  <ul class="list" style="left:455px;top:602px;width:300px">
    <li>Mixed Yoghurts <span class="price">$5.50</span></li>
    <li>Chia Pudding <span class="price">$5.50</span></li>
    <li>Fruit Salad <span class="price">$5.50</span></li>
    <li>Bircher Muesli <span class="price">$5.50</span></li>
    <li>Protein Balls <span class="price">$4.0</span></li>
    <li>Banana Bread <span class="price">$4.50</span></li>
    <li>Muffins <span class="price">$4.50</span></li>
    <li>Slices <span class="price">$4.0</span></li>
  </ul>

  <!-- Hot Food and Sandwiches -->
  <div class="ribbon" style="left:860px;top:450px;width:322px;height:84px;transform:rotate(-2deg)">
    <svg viewBox="0 0 322 84" preserveAspectRatio="none" aria-hidden="true">
      <polygon points="0,36 60,36 60,80 0,80 20,58" fill="var(--mint-dark)"/>
      <polygon points="322,36 262,36 262,80 322,80 302,58" fill="var(--mint-dark)"/>
      <path d="M40,12 Q161,-4 282,12 L282,64 Q161,48 40,64 Z" fill="var(--mint)"/>
    </svg>
    <div class="ribbon__label">Hot Food and Sandwiches</div>
  </div>

  <ul class="list" style="left:845px;top:541px;width:330px">
    <li>Pre Made Sandwiches <span class="price">$6.50 - $7.50</span></li>
    <li>Pre Made Focaccias <span class="price">$8.50</span></li>
    <li>Wraps <span class="price">$7.50</span></li>
    <li>Vegetarian Salad <span class="price">$7.50</span></li>
    <li>Meat/Seafood Salad <span class="price">$9.50</span></li>
    <li>Hot Chips <span class="price">$4.50</span></li>
    <li>Dim Sim <span class="price">$1.50</span></li>
    <li>Potato Cake <span class="price">$1.50</span></li>
    <li>Plain Hamburger <span class="price">$7.50</span></li>
    <li>Hamburger with the lot <span class="price">$9.0</span></li>
    <li>Chicken Schnitzel Burger <span class="price">$8.50</span></li>
  </ul>

</main>
</body>
</html>
```